VARLEN Consulting Services “Coming Soon” Landing Page

MORE INTO IN Design Brief for Web Designer document attached

1. Project Overview
Client: VARLEN Consulting Services
Project: Build a static, responsive “Coming Soon” landing page (HTML/CSS/JS)
Timeline: Target launch date in June 7, 2025
Point of Contact: Martin Hallowby (Managing Director)
 • Email: mart@varlenconsulting.example
 • Phone: 415-738-2094
Background:
VARLEN Consulting Services is a boutique IT consultancy specializing in enterprise cloud solutions, microservices, FlowMesh migrations, and AGENTIC AI-driven integrations. We are launching a new website to capture CIO-level leads, build brand awareness, and communicate our key value propositions before the full site goes live. This “Coming Soon” page should reflect our brand identity, target CIO and enterprise IT leaders, and collect email addresses for early access to whitepapers, case studies, and consultations.

2. Goals & Objectives
1. Brand Reinforcement
• Convey a contemporary, corporate, and professional look that aligns with VARLEN’s positioning as a specialized, agile, high-ROI consultancy.
• Utilize our brand colors (green, red, blue, gold) and typography (Segoe UI) consistently.
2. Lead Generation
• Implement a simple email-capture form (“Notify Me”) that submits to mailto:info@varlenconsulting.example.
• Convey clear messaging so visitors understand why they should sign up (exclusive early insights, whitepapers, invitations to consult).
3. Enterprise Leadership-Focused Messaging
• Immediately communicate our core value proposition (“Enterprise Modernization Reimagined”) and differentiation versus larger consulting firms.
• Introduce AGENTIC AI use cases to demonstrate cutting-edge capabilities.
4. Responsive & Accessible
• Build a mobile-first responsive design using a 12-column grid.
• Follow best practices for HTML5 markup, CSS3, and lightweight JS (for countdown timer).
5. SEO & Technical Must-Haves
• Include basic SEO metadata and Open Graph tags.
• Provide a favicon placeholder.
• Placeholder for a Privacy Policy link in the footer.

Designs look the same

VARLEN Consulting Services is a boutique IT consultancy specializing in enterprise cloud solutions, microservices, FlowMesh migrations, and AGENTIC AI-driven integrations.

• Below are our primary brand colors with hex codes (derived from CMYK values in the uploaded “Color and Font.jpg”): • Green (Globe Icon): #3BFF05 • Red (Q-Shape Icon): #EF1C03 • Blue (Circle Icon): #456EFF • Gold (Connector Icon): #F7C217 • Dark Gray / Text Color: #1A1A1A Use these colors for text highlights, buttons, icons, and accents. The overall page background is white or very light gray (#F9F9F9) to keep the design clean.
• Colors outside the scheme provided

```html
<!DOCTYPE html>
<html lang="en">
<head>
<meta charset="utf-8">
<title>VARLEN Consulting Services — Coming Soon</title>
<link rel="stylesheet" href="https://fonts.googleapis.com/css2?family=Open+Sans:wght@400;600;700;800&display=swap">
<style>
:root{
  --blue:#456eff;
  --blue-dark:#2f55e6;
  --green:#3bff05;
  --ink:#1a1a1a;
  --navy:#07122e;
  --navy-2:#0c1e4a;
  --night:#0d0d12;
  --muted:#5b5b66;
  --line:#cfd3dc;
  --white:#ffffff;
}
*{box-sizing:border-box;margin:0;padding:0}
html,body{width:1200px;height:4276px;overflow:hidden}
body{font-family:"Open Sans","Segoe UI",sans-serif;color:var(--ink);background:#fff;position:relative}
.abs{position:absolute}
.btn{position:absolute;display:flex;align-items:center;justify-content:center;background:var(--blue);color:#fff;border-radius:30px;font-size:15px;font-weight:600;height:44px}
.btn.ghost{background:transparent;border:2px solid #fff}
.section-title{position:absolute;font-size:30px;font-weight:800;letter-spacing:.5px}
.section-title::after{content:"";display:block;width:150px;height:3px;background:var(--blue);margin-top:6px}

/* hero */
.hero{position:absolute;left:0;top:0;width:1200px;height:760px;
  background:radial-gradient(ellipse 520px 300px at 980px 560px,rgba(69,110,255,.55),transparent 70%),
  radial-gradient(ellipse 700px 380px at 300px 700px,rgba(40,90,220,.35),transparent 70%),
  linear-gradient(180deg,#06112b 0%,#0b2258 60%,#0a1a44 100%)}
.brand{position:absolute;display:flex;align-items:center;gap:12px;color:#fff}
.brand .mark{width:46px;height:46px;border-radius:50%;background:#fff}
.brand .name{font-size:30px;font-weight:800;line-height:1}
.brand .tag{font-size:13px;font-weight:400;line-height:1.2}
.nav{position:absolute;left:400px;top:64px;display:flex;gap:44px;font-size:15px;color:#fff}
.nav a{color:#fff;text-decoration:none}
.nav a.active{border-bottom:2px solid #fff;padding-bottom:4px}
.hero h1{position:absolute;left:60px;top:226px;color:#fff;font-size:60px;font-weight:800;line-height:1.05}
.hero .soon{position:absolute;left:480px;top:238px;color:var(--green);font-size:34px;font-weight:700}
.hero .sub{position:absolute;left:60px;top:372px;width:900px;color:var(--green);font-size:27px;font-weight:700;line-height:1.35}
.hero .lede{position:absolute;left:60px;top:510px;width:1060px;color:#dfe6f7;font-size:14px;line-height:1.55}

/* about */
.about p{position:absolute;left:60px;width:560px;font-size:15px;line-height:1.6;color:#333}
.feature{position:absolute;width:110px;text-align:center;font-size:13px;font-weight:600;line-height:1.3}
.feature svg{display:block;margin:0 auto 8px}
.about-visual{position:absolute;left:620px;top:940px;width:520px;height:300px;border-radius:24px;
  background:radial-gradient(circle at 70% 45%,#6fa6ff 0%,#2d5fd8 30%,#0c2a72 65%,#071a45 100%)}

/* countdown */
.countdown{position:absolute;left:60px;top:1360px;width:1080px;height:660px;border-radius:40px;overflow:hidden;
  background:radial-gradient(ellipse 500px 260px at 820px 250px,rgba(80,140,255,.55),transparent 70%),
  radial-gradient(ellipse 500px 200px at 200px 520px,rgba(60,120,255,.4),transparent 70%),
  linear-gradient(180deg,#050b1f,#0b1d4d 70%,#08153a)}
.pill-title{position:absolute;background:var(--blue);color:#fff;font-weight:800;font-size:26px;padding:8px 40px 8px 28px;border-radius:0 30px 30px 0}
.coming{position:absolute;left:0;width:1080px;top:170px;text-align:center;color:#fff;font-size:52px;font-weight:800}
.timer{position:absolute;left:70px;top:280px;width:940px;height:190px;border:6px solid var(--green);border-radius:28px;
  background:rgba(255,255,255,.2);display:flex;justify-content:space-around;align-items:center}
.unit{text-align:center;color:#fff;width:130px}
.unit b{display:block;font-size:78px;font-weight:700;line-height:1}
.unit span{display:block;font-size:16px;letter-spacing:1px;margin-top:8px}
.unit+.unit{border-left:2px solid rgba(255,255,255,.5)}

/* services */
.svc{position:absolute;width:150px;height:150px;border-radius:50%;border:10px solid var(--blue);background:#fff;
  box-shadow:0 0 0 4px #fff,0 0 0 7px var(--blue);display:flex;flex-direction:column;align-items:center;justify-content:center;text-align:center;font-size:12px;font-weight:700;line-height:1.2;padding:10px}
.svc svg{margin-bottom:4px}
.svc-note{position:absolute;width:170px;text-align:center;font-size:13px;color:#333;line-height:1.5}
.stem{position:absolute;width:2px;background:var(--blue)}
.dot{position:absolute;width:12px;height:12px;border-radius:50%;background:var(--blue)}

/* agentic */
.agentic{position:absolute;left:60px;top:2620px;width:1080px;height:560px;border-radius:40px;overflow:hidden;
  background:linear-gradient(120deg,#060d28 0%,#0a1b4b 55%,#0c2a6e 100%)}
.agentic-visual{position:absolute;right:0;top:0;width:520px;height:560px;
  background:radial-gradient(ellipse 260px 300px at 60% 50%,#5c8ddf,#23457f 55%,#0c1f4a 100%)}
.case{position:absolute;left:50px;width:480px;color:#fff;font-size:19px;display:flex;gap:26px;padding-bottom:14px;border-bottom:1px solid rgba(255,255,255,.25)}
.case i{font-style:normal;width:30px}

/* contact */
.field{position:absolute;border:1px solid var(--line);border-radius:6px;height:40px;padding:10px 14px;font-size:13px;color:#666;background:#fff}
.info{position:absolute;left:790px;top:3330px;width:350px;height:290px;border-radius:18px;background:var(--blue);color:#fff}
.info h3{position:absolute;left:24px;top:18px;font-size:22px;font-weight:800}
.info-row{position:absolute;left:22px;width:300px;height:48px;border-radius:24px;background:#fff;color:var(--ink);display:flex;align-items:center;gap:12px;padding-left:10px;font-size:13px}
.info-row .ic{width:30px;height:30px;border-radius:50%;background:var(--blue);display:flex;align-items:center;justify-content:center}

/* footer */
.footer{position:absolute;left:0;top:3720px;width:1200px;height:556px;background:var(--night);color:#fff}
.footer p{position:absolute;font-size:13px;line-height:1.6;color:#d8d8d8}
.fcol{position:absolute;font-size:13px;line-height:2.7}
.fcol h4{font-size:24px;font-weight:600;line-height:1.4;margin-bottom:6px}
.social{position:absolute;width:28px;height:28px;border-radius:50%;background:#fff}
</style>
</head>
<body>

<!-- Hero -->
<header class="hero">
  <div class="brand" style="left:60px;top:44px">
    <div class="mark"></div>
    <div><div class="name">VARLEN</div><div class="tag">Consulting Services</div></div>
  </div>
  <nav class="nav">
    <a class="active">Home</a><a>About Us</a><a>Cooldown Time</a><a>Core Services</a><a>Use Cases</a>
  </nav>
  <div class="btn" style="left:1000px;top:52px;width:150px">Contact Us</div>
  <h1>ENTERPRISE<br>MODERNIZATION REIMAGINED</h1>
  <div class="soon">Coming Soon — Launching June 2025</div>
  <div class="sub">Retire Legacy Systems And Transition To Secure Cloud Native Infrastructure Designed For Scalability AI Integration And Future-Ready Performance</div>
  <p class="lede">Today's leaders don't have time for theoretical strategies and slow-moving firms. At VARLEN, we deliver tailored solutions that align with your business objectives, accelerate innovation, and scale as you grow. Our senior experts work directly with your team to deliver fast, measurable impact—no layers, no delays. From modernizing legacy platforms to enabling intelligent automation, we solve the complex integration challenges others overlook—so you can focus on leading the future.</p>
  <div class="btn" style="left:60px;top:620px;width:150px">Booking Now</div>
  <div class="btn ghost" style="left:240px;top:620px;width:150px">Read More</div>
</header>

<!-- About -->
<section class="about">
  <h2 class="section-title" style="left:60px;top:850px">ABOUT US</h2>
  <div class="btn" style="left:420px;top:848px;width:150px">Booking Now</div>
  <p style="top:920px">Imagine a partner that doesn't hand you a recycled playbook—but builds a smarter path forward that's all about your goals. At VARLEN Consulting Services, we don't do cookie-cutter. We roll up our sleeves, work alongside your team, and deliver fast, measurable results that move the needle. While others push templates, we unlock possibilities—modern systems, real efficiency, and AI that actually works. No fluff. No junior handoffs. Just bold execution that gets you ahead—and keeps you there.</p>
  <p style="top:1090px">VARLEN is a boutique IT consulting firm specializing in enterprise modernization. We help CIOs and IT leaders transform legacy systems using cloud, microservices and agentic AI solutions.</p>
  <div class="feature" style="left:50px;top:1170px">
    <svg width="40" height="36" viewBox="0 0 40 36" fill="none" stroke="#1a1a1a" stroke-width="2"><path d="M6 30h28M10 30V14h20v16M20 4l14 10H6z"/></svg>Senior Access Always</div>
  <div class="feature" style="left:180px;top:1170px">
    <svg width="40" height="36" viewBox="0 0 40 36" fill="none" stroke="#1a1a1a" stroke-width="2"><path d="M6 30a14 14 0 0 1 28 0M20 30l8-12"/></svg>Speed That Scales</div>
  <div class="feature" style="left:310px;top:1170px">
    <svg width="40" height="36" viewBox="0 0 40 36" fill="none" stroke="#1a1a1a" stroke-width="2"><circle cx="20" cy="12" r="8"/><path d="M16 20v10h8V20"/></svg>Custom Paths To Modernization</div>
  <div class="feature" style="left:440px;top:1170px">
    <svg width="40" height="36" viewBox="0 0 40 36" fill="none" stroke="#1a1a1a" stroke-width="2"><path d="M20 4v28M8 10h24M8 10l-4 10h8zM32 10l-4 10h8z"/></svg>Custom Paths To Modernization</div>
  <div class="about-visual" role="img" aria-label="Hand holding a glowing digital globe with network lines"></div>
</section>

<!-- Countdown -->
<section class="countdown" role="img" aria-label="Dark blue digital wave background" >
  <div class="pill-title" style="left:0;top:40px">COOLDOWN TIMER</div>
  <div class="btn" style="left:860px;top:44px;width:150px">Booking Now</div>
  <div class="coming">COMING SOON</div>
  <div class="timer">
    <div class="unit"><b>24</b><span>MONTHS</span></div>
    <div class="unit"><b>24</b><span>WEEKS</span></div>
    <div class="unit"><b>24</b><span>DAYS</span></div>
    <div class="unit"><b>24</b><span>HOURS</span></div>
    <div class="unit"><b>24</b><span>MINUTS</span></div>
    <div class="unit"><b>24</b><span>SECONDS</span></div>
  </div>
</section>

<!-- Core services -->
<section class="services">
  <h2 class="section-title" style="left:60px;top:2060px">CORE SERVICES</h2>
  <div class="btn" style="left:970px;top:2058px;width:170px">Booking Now</div>

  <div class="svc" style="left:65px;top:2130px">
    <svg width="30" height="30" viewBox="0 0 30 30" fill="none" stroke="#1a1a1a" stroke-width="2"><rect x="3" y="3" width="10" height="10"/><rect x="17" y="3" width="10" height="10"/><rect x="10" y="17" width="10" height="10"/></svg>Microservices Architecture</div>
  <div class="svc" style="left:465px;top:2110px">
    <svg width="30" height="30" viewBox="0 0 30 30" fill="none" stroke="#1a1a1a" stroke-width="2"><circle cx="15" cy="15" r="11"/><path d="M4 15h22M15 4c5 6 5 16 0 22M15 4c-5 6-5 16 0 22"/></svg>Nimbus Integration Architecture</div>
  <div class="svc" style="left:805px;top:2110px">
    <svg width="30" height="30" viewBox="0 0 30 30" fill="none" stroke="#1a1a1a" stroke-width="2"><path d="M5 20a8 8 0 0 1 3-14 9 9 0 0 1 16 4 6 6 0 0 1 0 10z"/><path d="M15 14v10M11 20l4 4 4-4"/></svg>FlowMesh Migration &amp; Optimization</div>
  <div class="svc" style="left:265px;top:2345px">
    <svg width="30" height="30" viewBox="0 0 30 30" fill="none" stroke="#1a1a1a" stroke-width="2"><circle cx="8" cy="15" r="5"/><circle cx="22" cy="15" r="5"/><path d="M13 15h4"/></svg>Hybrid Integration Solutions</div>
  <div class="svc" style="left:605px;top:2345px">
    <svg width="30" height="30" viewBox="0 0 30 30" fill="none" stroke="#1a1a1a" stroke-width="2"><rect x="7" y="7" width="16" height="16" rx="2"/><path d="M11 3v4M19 3v4M11 23v4M19 23v4M3 11h4M3 19h4M23 11h4M23 19h4"/></svg>AGENTIC AI Enablement</div>
  <div class="svc" style="left:973px;top:2345px">
    <svg width="30" height="30" viewBox="0 0 30 30" fill="none" stroke="#1a1a1a" stroke-width="2"><rect x="3" y="5" width="24" height="16" rx="2"/><path d="M10 27h10M15 21v6"/></svg>Technical Training</div>

  <div class="stem" style="left:263px;top:2210px;height:130px"></div><div class="dot" style="left:258px;top:2204px"></div>
  <div class="svc-note" style="left:60px;top:2320px">Fault Tolerant, Scalable Services That Integrate With Legacy</div>
  <div class="svc-note" style="left:230px;top:2210px;left:290px">Fault Tolerant, Scalable Services That Integrate With Legacy</div>

  <div class="stem" style="left:680px;top:2275px;height:70px"></div><div class="dot" style="left:675px;top:2270px"></div>
  <div class="svc-note" style="left:600px;top:2205px">Fault Tolerant, Scalable Services That Integrate With Legacy</div>
  <div class="svc-note" style="left:420px;top:2300px">Fault Tolerant, Scalable Services That Integrate With Legacy</div>

  <div class="stem" style="left:1047px;top:2190px;height:155px"></div><div class="dot" style="left:1042px;top:2185px"></div>
  <div class="svc-note" style="left:955px;top:2205px;left:960px;top:2210px;width:180px;left:940px;display:none"></div>
  <div class="svc-note" style="left:995px;top:2210px;left:990px;width:150px">Fault Tolerant, Scalable Services That Integrate With Legacy</div>
  <div class="svc-note" style="left:800px;top:2300px">Fault Tolerant, Scalable Services That Integrate With Legacy</div>
</section>

<!-- Agentic AI -->
<section class="agentic">
  <div class="agentic-visual" role="img" aria-label="Business professional holding a tablet with glowing digital network overlay"></div>
  <div class="pill-title" style="left:0;top:40px">AGENTIC AI USE CASES</div>
  <div class="case" style="top:130px"><i>01</i>Autonomous Exception Handling</div>
  <div class="case" style="top:200px"><i>02</i>Dynamic Workflow Optimization</div>
  <div class="case" style="top:270px"><i>03</i>Predictive Modernization Scaling</div>
  <div class="case" style="top:340px"><i>04</i>Real-Time Compliance &amp; Audit Trail Agents</div>
  <div class="btn" style="left:50px;top:450px;width:150px">Booking Now</div>
</section>

<!-- Contact -->
<section class="contact">
  <h2 class="section-title" style="left:60px;top:3270px">CONTACT US</h2>
  <div class="field" style="left:60px;top:3335px;width:350px">Full Name</div>
  <div class="field" style="left:425px;top:3335px;width:350px">Date</div>
  <div class="field" style="left:60px;top:3390px;width:350px">Email</div>
  <div class="field" style="left:425px;top:3390px;width:350px">Phone</div>
  <div class="field" style="left:60px;top:3445px;width:715px;height:160px">Message</div>
  <div class="btn" style="left:60px;top:3630px;width:150px">Submit Now</div>
  <div class="info">
    <h3>INFO</h3>
    <div class="info-row" style="top:80px"><span class="ic"><svg width="14" height="14" viewBox="0 0 14 14" fill="#fff"><path d="M3 1l2 3-1.5 1.5a8 8 0 0 0 5 5L10 9l3 2-1 2C6 13 1 8 1 2z"/></svg></span>415-738-2094</div>
    <div class="info-row" style="top:145px"><span class="ic"><svg width="14" height="12" viewBox="0 0 14 12" fill="none" stroke="#fff" stroke-width="1.5"><rect x="1" y="1" width="12" height="10"/><path d="M1 1l6 5 6-5"/></svg></span>mart@varlenconsulting.example</div>
    <div class="info-row" style="top:210px"><span class="ic"><svg width="12" height="14" viewBox="0 0 12 14" fill="#fff"><path d="M6 0a5 5 0 0 1 5 5c0 4-5 9-5 9S1 9 1 5a5 5 0 0 1 5-5z"/><circle cx="6" cy="5" r="2" fill="#456eff"/></svg></span>Wood Street Block City</div>
  </div>
</section>

<!-- Footer -->
<footer class="footer">
  <div class="brand" style="left:60px;top:60px">
    <div class="mark" style="width:70px;height:70px"></div>
    <div><div class="name" style="font-size:48px">VARLEN</div><div class="tag" style="font-size:20px">Consulting Services</div></div>
  </div>
  <p style="left:60px;top:190px;width:440px">Lorem ipsum dolor sit amet consectetur. Eget mauris ac lacinia pellentesque magna. Sed sem dui aliquam convallis. Vitae eget enim ornare mauris non bibendum nisi.</p>
  <p style="left:60px;top:270px;width:480px">LinkedIn: https://www.example.com/company/varlen</p>
  <p style="left:60px;top:300px;width:480px">Email: mailto:info@varlenconsulting.example</p>
  <div class="fcol" style="left:860px;top:50px"><h4>Quik Link</h4>Home<br>About Us<br>Cooldown Time<br>Core Service<br>Agentic AI Use Cases<br>Contact Us</div>
  <div class="fcol" style="left:1020px;top:50px"><h4>Legal</h4>Privacy Policy<br>Terms Of Use<br>Cookie Policy</div>
  <div class="social" style="left:60px;top:410px"></div>
  <div class="social" style="left:104px;top:410px"></div>
  <div class="social" style="left:148px;top:410px"></div>
  <div class="social" style="left:192px;top:410px"></div>
  <div class="social" style="left:236px;top:410px"></div>
  <div class="abs" style="left:0;top:460px;width:1200px;height:1px;background:#333"></div>
  <p style="left:860px;top:412px">Copyright © 2025 All Right Reserved</p>
</footer>

</body>
</html>
```